TalkWell needs a Letterhead

We need a letterhead for our company "TalkWell Consultants". Logo is attached. The company color is Turquoise. Icons for website, scan logo for website, icons for address, e-mail and phone appreciated rather than just words.

```html
<!DOCTYPE html>
<html lang="en">
<head>
<meta charset="utf-8">
<title>TalkWell Consultants Letterhead</title>
<link href="https://fonts.googleapis.com/css2?family=Questrial&display=swap" rel="stylesheet">
<style>
  :root {
    --brand-blue: #1075bb;
    --brand-green: #8cc63f;
    --mark-tint: #e5eff8;
    --paper: #ffffff;
  }
  * { margin: 0; padding: 0; box-sizing: border-box; }
  html, body { width: 849px; height: 1200px; overflow: hidden; background: var(--paper); }
  .letterhead {
    position: relative;
    width: 849px;
    height: 1200px;
    background: var(--paper);
    font-family: "Questrial", "Century Gothic", sans-serif;
    overflow: hidden;
  }
  .band { position: absolute; }
  .band--blue { background: var(--brand-blue); }
  .band--green { background: var(--brand-green); }

  .header-left-blue { left: 0; top: 66px; width: 38px; height: 27px; }
  .header-left-green { left: 0; top: 103px; width: 38px; height: 15px; }
  .header-right-blue { left: 461px; top: 67px; width: 388px; height: 31px; }
  .header-right-green { left: 461px; top: 103px; width: 388px; height: 16px; }

  .brand {
    position: absolute;
    left: 60px;
    top: 60px;
    display: flex;
    align-items: center;
    gap: 14px;
  }
  .brand-square {
    width: 46px;
    height: 46px;
    background: var(--brand-blue);
  }
  .brand-name {
    color: var(--brand-blue);
    font-size: 33px;
    line-height: 1;
    white-space: nowrap;
  }

  .watermark-name {
    position: absolute;
    left: 0;
    width: 849px;
    top: 595px;
    text-align: center;
    color: var(--mark-tint);
    font-size: 96px;
    line-height: 1;
    white-space: nowrap;
  }

  .footer-left-blue { left: 0; top: 1132px; width: 161px; height: 25px; }
  .footer-left-green { left: 0; top: 1162px; width: 161px; height: 11px; }
  .footer-right-blue { left: 824px; top: 1132px; width: 25px; height: 25px; }
  .footer-right-green { left: 824px; top: 1162px; width: 25px; height: 11px; }

  .contact {
    position: absolute;
    display: flex;
    align-items: center;
    gap: 9px;
    white-space: nowrap;
    line-height: 1;
  }
  .contact svg { flex: none; }
  .contact--primary { top: 1131px; color: var(--brand-blue); font-size: 18px; }
  .contact--secondary { top: 1160px; color: var(--brand-green); font-size: 15px; }
  .contact-phone { left: 172px; }
  .contact-fax { left: 378px; }
  .contact-email { left: 599px; }
  .contact-web { left: 174px; }
  .contact-address { left: 380px; }
</style>
</head>
<body>
<main class="letterhead">
  <header>
    <div class="band band--blue header-left-blue"></div>
    <div class="band band--green header-left-green"></div>
    <div class="brand">
      <div class="brand-square"></div>
      <span class="brand-name">TalkWell Consultants</span>
    </div>
    <div class="band band--blue header-right-blue"></div>
    <div class="band band--green header-right-green"></div>
  </header>

  <div class="watermark-name" aria-hidden="true">TalkWell</div>

  <footer>
    <div class="band band--blue footer-left-blue"></div>
    <div class="band band--green footer-left-green"></div>
    <div class="band band--blue footer-right-blue"></div>
    <div class="band band--green footer-right-green"></div>

    <div class="contact contact--primary contact-phone">
      <svg width="17" height="17" viewBox="0 0 24 24" fill="currentColor"><path d="M6.6 10.8a15.1 15.1 0 0 0 6.6 6.6l2.2-2.2a1 1 0 0 1 1-.25 11.4 11.4 0 0 0 3.6.57 1 1 0 0 1 1 1V20a1 1 0 0 1-1 1A17 17 0 0 1 3 4a1 1 0 0 1 1-1h3.5a1 1 0 0 1 1 1c0 1.25.2 2.45.57 3.57a1 1 0 0 1-.25 1z"/></svg>
      <span>+91 9000012345</span>
    </div>
    <div class="contact contact--primary contact-fax">
      <svg width="16" height="17" viewBox="0 0 20 22" fill="currentColor"><rect x="0" y="6" width="5" height="15" rx="1"/><path d="M6 6h13a1 1 0 0 1 1 1v13a1 1 0 0 1-1 1H6z"/><rect x="8" y="0" width="9" height="5" rx="1"/><g fill="#fff"><rect x="8" y="9" width="9" height="3"/><rect x="8" y="14" width="2" height="2"/><rect x="11.5" y="14" width="2" height="2"/><rect x="15" y="14" width="2" height="2"/><rect x="8" y="17" width="2" height="2"/><rect x="11.5" y="17" width="2" height="2"/><rect x="15" y="17" width="2" height="2"/></g></svg>
      <span>+9122 20001234</span>
    </div>
    <div class="contact contact--primary contact-email">
      <svg width="17" height="12" viewBox="0 0 24 16" fill="currentColor"><path d="M0 0h24v16H0z"/><path d="M1 1l11 8 11-8" fill="none" stroke="#fff" stroke-width="1.6"/></svg>
      <span>talkwell@mailbox.com</span>
    </div>

    <div class="contact contact--secondary contact-web">
      <svg width="14" height="14" viewBox="0 0 24 24" fill="none" stroke="currentColor" stroke-width="1.8"><circle cx="12" cy="12" r="10"/><ellipse cx="12" cy="12" rx="4.5" ry="10"/><path d="M2 12h20M4 6.5h16M4 17.5h16"/></svg>
      <span>www.talkwell.com</span>
    </div>
    <div class="contact contact--secondary contact-address">
      <svg width="11" height="15" viewBox="0 0 16 22" fill="currentColor"><path d="M8 0a8 8 0 0 0-8 8c0 6 8 14 8 14s8-8 8-14a8 8 0 0 0-8-8zm0 11a3 3 0 1 1 0-6 3 3 0 0 1 0 6z"/></svg>
      <span>No.12, K 4th Cross, Bangalore, Karnataka - 560001.</span>
    </div>
  </footer>
</main>
</body>
</html>
```